KBR, LLC Original

I need a business card design for a new company in Gaithersburg, MD. Though the name of the company is Wiring By Candor (KBR) we specialize in commercial kitchen ventilation systems as a complete turnkey project or as a service provider. We can design the entire system including the hoods, fans, ductwork, and fire system. We also specialize in fire alarm service, design, install and inspection. We are experts on any Pellmoor Units equipment including Vexa PCU, Vexa Hoods, EMS controls, Standard controls, PCU filtration and Make-up Air units with heaters and cooling. We can repair/retrofit old water wash hood systems as well. We are experts with local code requirements and upgrades.

Industry/Entity Type

Business

Contact Information for Business Card

Neil Radcott, Wiring By Candor, LLC; 240-555-0182 Cell, Brinwood, MD 20999. Neilr@wiringbycandorco.example

```html
<!DOCTYPE html>
<html lang="en">
<head>
<meta charset="utf-8">
<title>Wiring By Candor, LLC — Business Card</title>
<link rel="stylesheet" href="https://fonts.googleapis.com/css2?family=Lato:wght@400;700;900&display=swap">
<style>
  :root {
    --backdrop: #d9d9d9;
    --card-shadow: rgba(0, 0, 0, 0.22);
    --steel-dark: #3a3a36;
    --steel-mid: #8d8a7c;
    --steel-light: #cfcabb;
    --tile-warm: #a89a74;
    --band-black: #000000;
    --band-text: #ffffff;
    --pale-1: #f4f3ef;
    --pale-2: #e6e4dd;
    --pale-3: #d8d6ce;
    --ink: #000000;
    --ink-soft: #111111;
  }

  * { box-sizing: border-box; margin: 0; padding: 0; }

  html, body {
    width: 1200px;
    height: 926px;
    overflow: hidden;
    background: var(--backdrop);
    font-family: "Lato", Arial, sans-serif;
  }

  .sheet {
    position: relative;
    width: 1200px;
    height: 926px;
  }

  .card {
    position: absolute;
    left: 250px;
    width: 700px;
    height: 400px;
    overflow: hidden;
    box-shadow: 0 10px 28px var(--card-shadow);
  }

  .card--front { top: 42px; }
  .card--back  { top: 484px; }

  /* Front */
  .kitchen-photo {
    position: absolute;
    inset: 0;
    background:
      linear-gradient(180deg, rgba(0,0,0,0.25) 0%, rgba(0,0,0,0) 30%, rgba(0,0,0,0) 70%, rgba(0,0,0,0.35) 100%),
      linear-gradient(100deg, var(--steel-dark) 0%, var(--tile-warm) 22%, var(--steel-light) 42%, var(--steel-mid) 62%, var(--steel-light) 78%, var(--steel-dark) 100%);
  }

  .name-band {
    position: absolute;
    left: 200px;
    right: 0;
    top: 228px;
    height: 92px;
    background: var(--band-black);
    color: var(--band-text);
    padding: 10px 18px 0 22px;
  }

  .company-name {
    font-size: 37px;
    font-weight: 700;
    letter-spacing: 0.3px;
    line-height: 1.1;
    white-space: nowrap;
  }

  .company-name .suffix { font-weight: 400; }

  .tagline {
    margin-top: 6px;
    font-size: 17px;
    font-weight: 700;
    letter-spacing: 0.4px;
    white-space: nowrap;
  }

  /* Back */
  .kitchen-photo--faded {
    position: absolute;
    inset: 0;
    background:
      linear-gradient(100deg, var(--pale-1) 0%, var(--pale-2) 30%, var(--pale-1) 50%, var(--pale-3) 72%, var(--pale-2) 100%);
  }

  .person-name {
    position: absolute;
    left: 110px;
    top: 92px;
    font-size: 54px;
    font-weight: 900;
    letter-spacing: 1px;
    color: var(--ink);
    white-space: nowrap;
  }

  .contact-lines {
    position: absolute;
    left: 26px;
    top: 230px;
    font-size: 19px;
    line-height: 1.35;
    color: var(--ink-soft);
  }

  .address {
    position: absolute;
    right: 30px;
    bottom: 34px;
    text-align: right;
    font-size: 21px;
    line-height: 1.3;
    color: var(--ink-soft);
  }
</style>
</head>
<body>
  <main class="sheet">
    <section class="card card--front">
      <div class="kitchen-photo" role="img" aria-label="Photograph of a stainless steel commercial kitchen with ventilation hoods"></div>
      <div class="name-band">
        <p class="company-name">Wiring By Candor, <span class="suffix">LLC</span></p>
        <p class="tagline">we specialize in commercial kitchen ventilation systems</p>
      </div>
    </section>

    <section class="card card--back">
      <div class="kitchen-photo--faded" role="img" aria-label="Faded photograph of a commercial kitchen used as a light background"></div>
      <h1 class="person-name">Neil Radcott</h1>
      <p class="contact-lines">240-555-0182<br>Neilr@wiringbycandorco.example</p>
      <p class="address">Brinwood,<br>MD 20999</p>
    </section>
  </main>
</body>
</html>
```